TERRAVOL " need somthing eye catching and envirnmental friendely materials

Business Card " UNIQUE..
- use the agreed on logo.
- use wooden background.
- the environmental sound should be HIGH.

Company slogan is ZERO DISCHARGE.
We work in deploying the latest technology “ USA & Europe” in the field of drill cutting recycle and economically managing the footprint.
With the ramp up in oil demands and the increase in oil prices , operators are extending their operations into new geographical areas “ government regulations and eco-sounds” created the need to a specialty services and products that should go parallel or even ahead.

Target Market(s)

OIL field and environmental concerned.
Mainly ENGINEERS.

Industry/Entity Type

Government

Font styles to use
Decorative
Script

Colors

Designer to choose colors to be used in the design.

Requirements
Must have
• Eco - sounded.

```html
<!DOCTYPE html>
<html lang="en">
<head>
<meta charset="utf-8">
<title>TERRAVOL Business Card</title>
<link href="https://fonts.googleapis.com/css2?family=Exo+2:ital,wght@0,400;0,600;0,700;1,800&display=swap" rel="stylesheet">
<style>
  :root{
    --backdrop:#2a1a10;
    --wood-light:#e4e4e2;
    --wood-dark:#a9a9a7;
    --ink:#141414;
    --night:#1b1b1b;
    --night-soft:#3a3a3a;
    --leaf:#4a9a2e;
    --lime:#9ac93c;
    --gold:#c9922a;
    --paper:#ffffff;
  }
  *{box-sizing:border-box;margin:0;padding:0}
  html,body{width:1200px;height:1000px;overflow:hidden}
  body{background:var(--backdrop);font-family:"Exo 2",sans-serif;position:relative}
  .card{position:absolute;width:560px;height:330px;border-radius:18px;overflow:hidden;box-shadow:0 10px 30px rgba(0,0,0,.5)}
  .card--front{left:30px;top:110px}
  .card--green{left:610px;top:110px;background:var(--lime)}
  .card--white{left:320px;top:560px;background:var(--paper)}
  .card-art{position:absolute;inset:0;width:100%;height:100%}
  .brand{position:absolute;display:flex;align-items:center;gap:10px;font-weight:700;letter-spacing:1px;color:var(--leaf)}
  .brand-dot{width:22px;height:22px;border-radius:50%;background:var(--leaf)}
  .card--front .brand{left:36px;top:90px;font-size:30px}
  .card--green .brand{left:150px;top:115px;font-size:40px;color:var(--ink)}
  .card--green .brand-dot{background:var(--ink)}
  .card--white .brand{left:150px;top:110px;font-size:40px}
  .holder{position:absolute;right:40px;top:34px;text-align:right}
  .holder-name{font-size:24px;font-weight:600;color:var(--ink);letter-spacing:1px}
  .holder-role{font-size:17px;color:var(--leaf);letter-spacing:.5px}
  .contacts{position:absolute;left:334px;top:224px;list-style:none;color:#fff}
  .contacts li{display:flex;align-items:center;gap:10px;height:32px;font-size:16px;letter-spacing:.5px}
  .contacts li:first-child{font-size:19px}
  .contacts svg{width:16px;height:16px;flex:none}
  .slogan{position:absolute;left:60px;bottom:24px;font-size:18px;font-weight:800;font-style:italic;letter-spacing:2px;color:var(--gold)}
  .site{position:absolute;font-size:16px;font-weight:600;color:var(--ink);letter-spacing:.5px}
  .card--green .site{left:150px;top:190px}
  .card--white .site{left:150px;top:190px}
</style>
</head>
<body>

<article class="card card--front">
  <svg class="card-art" viewBox="0 0 560 330" preserveAspectRatio="none">
    <defs>
      <linearGradient id="wood" x1="0" y1="0" x2="1" y2="1">
        <stop offset="0" stop-color="#e4e4e2"/><stop offset="1" stop-color="#a9a9a7"/>
      </linearGradient>
      <linearGradient id="night" x1="0" y1="0" x2="0" y2="1">
        <stop offset="0" stop-color="#3a3a3a"/><stop offset=".4" stop-color="#1b1b1b"/><stop offset="1" stop-color="#111"/>
      </linearGradient>
    </defs>
    <rect width="560" height="330" fill="url(#wood)" role="img" aria-label="Grey wooden planks background"/>
    <path d="M0,215 C160,150 380,130 560,150 L560,330 L0,330 Z" fill="var(--leaf)"/>
    <path d="M0,232 C160,170 380,150 560,170 L560,330 L0,330 Z" fill="#fff"/>
    <path d="M0,242 C160,182 380,165 560,186 L560,330 L0,330 Z" fill="url(#night)"/>
  </svg>
  <div class="brand"><span class="brand-dot"></span>TERRAVOL</div>
  <div class="holder">
    <p class="holder-name">KARIM NADER HASSAN</p>
    <p class="holder-role">Chief Executive Officer</p>
  </div>
  <ul class="contacts">
    <li><svg viewBox="0 0 16 16"><rect width="16" height="16" rx="4" fill="var(--leaf)"/><rect x="5" y="3" width="6" height="10" rx="1" fill="none" stroke="#fff" stroke-width="1.3"/></svg>009715 555 010 42</li>
    <li><svg viewBox="0 0 16 16"><rect width="16" height="16" rx="4" fill="var(--leaf)"/><rect x="3" y="5" width="10" height="7" fill="none" stroke="#fff" stroke-width="1.3"/><path d="M3 5 L8 9 L13 5" fill="none" stroke="#fff" stroke-width="1.2"/></svg>IT@TERRAVOL.com</li>
    <li><svg viewBox="0 0 16 16"><rect width="16" height="16" rx="8" fill="var(--leaf)"/><circle cx="8" cy="8" r="4.5" fill="none" stroke="#fff" stroke-width="1.2"/><path d="M3.5 8 H12.5 M8 3.5 V12.5" stroke="#fff" stroke-width="1"/></svg>www.TERRAVOL.ae</li>
  </ul>
  <p class="slogan">ZERO DISCHARGE</p>
</article>

<article class="card card--green">
  <div class="brand"><span class="brand-dot"></span>TERRAVOL</div>
  <p class="site">www.TERRAVOL.aet</p>
</article>

<article class="card card--white">
  <div class="brand"><span class="brand-dot"></span>TERRAVOL</div>
  <p class="site">www.TERRAVOL.aet</p>
</article>

</body>
</html>
```